Logo and Business card design!

Halvern Estates

We are a Property development and real estate company (needs a logo design).

Halvern estates is based in Sydney Australia and will be dealing with high net worth individuals with a corporate background. The demographic of clients will be relatively youthful and savvy. We do development finance, property development and some portion of property sales

I'd like the 'Halvern' part of the name to be strength of the title, with 'property' playing a very minor part, perhaps in tiny font somewhere off to the bottom or side or something

Thank you!

Target Market(s)

25-55 years old

Industry/Entity Type

Real Estate Development

Contact Information for Business Card

Please arrange this information as you see fit

Doug Pennicott
Managing Director
0417 582 330
doug@halvernestates.com.au
www.halvernestates.com.au

Logo Text

Halvern estates

Font styles to use
Serif

Colors

Designer to choose colors to be used in the design.

Requirements
Must have
• PLEASE VIEW THE UPLOADED IMAGES AND EXAMPLES
• And please put 'property' in small letters at the bottom or to the side. I want it to play a minimalist role, with 'HALVERN' being the feature
• Colours! Please make sure theyre mostly grey and white with possibly some other dark blue and maybe dark grey
Nice to have
• Please feel free to use whatever colors you like, the suggested colors are something I selected momentarily and dont necessarily reflect strict guidelines
Should not have
• NO pictures or shapes of houses. I dont want the logo design to be so literal in its imagery

```html
<!DOCTYPE html>
<html lang="en">
<head>
<meta charset="utf-8">
<title>Halvern Estates — Business Card</title>
<link rel="stylesheet" href="https://fonts.googleapis.com/css2?family=Open+Sans:wght@300;400;600&display=swap">
<style>
  :root {
    --stage: #5a5a5a;
    --card-dark: #333333;
    --card-light: #d4d4d4;
    --ink-dark: #3a3a3a;
    --ink-mid: #5c5c5c;
    --ink-white: #f4f4f4;
  }
  * { margin: 0; padding: 0; box-sizing: border-box; }
  html, body { width: 1200px; height: 904px; overflow: hidden; }
  body {
    background: var(--stage);
    font-family: "Open Sans", sans-serif;
    position: relative;
  }
  .card {
    position: absolute;
    width: 560px;
    height: 320px;
    box-shadow: 0 10px 24px rgba(0,0,0,.35);
  }
  .card--front {
    left: 110px; top: 96px;
    background: var(--card-dark);
    display: flex; align-items: center; justify-content: center;
  }
  .card--back {
    left: 530px; top: 488px;
    background: var(--card-dark);
    padding: 16px;
  }
  .card__face {
    position: relative;
    width: 100%; height: 100%;
    background: var(--card-light);
  }
  .brand {
    display: flex; align-items: center; gap: 14px;
  }
  .brand__mark {
    width: 22px; height: 22px;
  }
  .brand__name {
    font-weight: 300;
    font-size: 26px;
    letter-spacing: 6px;
    white-space: nowrap;
  }
  .card--front .brand__mark { background: var(--ink-white); }
  .card--front .brand__name { color: var(--ink-white); }
  .card--back .brand {
    position: absolute; left: 0; right: 0; top: 58px;
    justify-content: center;
  }
  .card--back .brand__mark { background: var(--ink-dark); }
  .card--back .brand__name { color: var(--ink-dark); }
  .contact {
    position: absolute; right: 28px; bottom: 38px;
    display: flex; align-items: center; gap: 16px;
  }
  .person { text-align: right; }
  .person__name {
    font-weight: 600; font-size: 15px; color: var(--ink-dark);
  }
  .person__role {
    font-weight: 400; font-size: 13px; color: var(--ink-mid);
  }
  .contact__rule {
    width: 1px; height: 58px; background: var(--ink-dark);
  }
  .details { list-style: none; }
  .details li {
    display: flex; align-items: center; gap: 7px;
    font-size: 12.5px; color: var(--ink-mid); line-height: 19px;
  }
  .details svg { width: 11px; height: 11px; fill: none; stroke: var(--ink-dark); stroke-width: 1.6; }
</style>
</head>
<body>
  <section class="card card--front">
    <div class="brand">
      <span class="brand__mark"></span>
      <span class="brand__name">HALVERN ESTATES</span>
    </div>
  </section>

  <section class="card card--back">
    <div class="card__face">
      <div class="brand">
        <span class="brand__mark"></span>
        <span class="brand__name">HALVERN ESTATES</span>
      </div>
      <div class="contact">
        <div class="person">
          <p class="person__name">Doug Pennicott</p>
          <p class="person__role">Managing Director</p>
        </div>
        <span class="contact__rule"></span>
        <ul class="details">
          <li>
            <svg viewBox="0 0 12 12"><path d="M3 1.5 L4.8 3.8 L3.8 5 Q5 7.2 7 8.2 L8.2 7.2 L10.5 9 L9.3 10.5 Q4.5 10 1.5 3 Z"/></svg>
            0417 582 330
          </li>
          <li>
            <svg viewBox="0 0 12 12"><rect x="1" y="2.5" width="10" height="7"/><path d="M1 2.5 L6 6.5 L11 2.5"/></svg>
            doug@halvernestates.com.au
          </li>
          <li>
            <svg viewBox="0 0 12 12"><circle cx="6" cy="6" r="4.8"/><path d="M1.2 6 H10.8 M6 1.2 Q3 6 6 10.8 M6 1.2 Q9 6 6 10.8"/></svg>
            www.halvernestates.com.au
          </li>
        </ul>
      </div>
    </div>
  </section>
</body>
</html>
```